Craft Flavoured Beer Family Extension Desing

We are a Canadian craft brewery looking for the design of a new line of beer we wish to launch within an existing family of products. Our beers are high craft beers that retail for a significant price. Example, 4.49$ for 500 mL vs. 1.49$ for a 500 mL Valdmeer.

The line of beer that is being designed here is for a craft flavoured beer line targeted to women. This will be light tasting beers with light fruit flavors targeted to consumers who like beer but are not ready for the strong IPA which are generally found in the craft beer offerings.

The Mireille line, which is the name of this new product, is a ''cousin'' of the existing Gustave-Armand Line (more info below).

Target Market(s)

60% Females 40% Males - 21 to 40 years old

Industry/Entity Type

Brewery

Requirements
Must have
• The products will be an INDIRECT family/line extension of the Gustave-Armand line of products (design attached). There needs to be some similarities, but it cannot be too close. There are 3 main features on the Gustave-Armand label (attached) : (1) the font used for the Logo; (2) the shape of the label; (3) the motif printed on the label.
• The shape of the label must be different than the current shape.
• However, the font of the logo (Gustave-Armand) can be the same and the motif printed on the label can be used. Using one of these elements is sufficient to link this new brand with the Gustave-Armand brand.
• The name of the product will be MIREILLE
Nice to have
• The bottle, the size, the ABV will be different than for the Gustave-Armand beers.
• There will be 3 flavours initially : Blueberry, Grapefruit and Raspberry.
• There needs to be a back label, but if you design, you can use the exact same information as there is currently.
Should not have
• We don't want any fruit pictures or designs on the labels.

```html
<!DOCTYPE html>
<html lang="fr">
<head>
<meta charset="utf-8">
<title>Mireille – Flavoured Beer Labels</title>
<link rel="stylesheet" href="https://fonts.googleapis.com/css2?family=Oswald:wght@600;700&family=Noto+Serif:wght@400;700&family=Roboto+Condensed:wght@700&display=swap">
<style>
  :root {
    --backdrop: #3b3b3c;
    --ink: #1e1e1e;
    --grapefruit: #d9772a;
    --grapefruit-paper: #f3f0e4;
    --blueberry: #3f72b5;
    --blueberry-paper: #dde8f3;
    --raspberry: #c2233f;
    --raspberry-paper: #f5dde3;
    --ribbon-text: #fdf8ee;
  }
  * { margin: 0; padding: 0; box-sizing: border-box; }
  html, body { width: 970px; height: 1200px; overflow: hidden; background: var(--backdrop); }
  .label-range {
    width: 970px; height: 1200px;
    display: flex; align-items: center; justify-content: center; gap: 25px;
  }
  .label { width: 290px; height: 470px; display: block; }
  .label--grapefruit { --accent: var(--grapefruit); --paper: var(--grapefruit-paper); }
  .label--blueberry  { --accent: var(--blueberry);  --paper: var(--blueberry-paper); }
  .label--raspberry  { --accent: var(--raspberry);  --paper: var(--raspberry-paper); }

  .label-edge { fill: var(--paper); stroke: var(--accent); stroke-width: 7; }
  .label-stitch { fill: none; stroke: var(--accent); stroke-width: 1; stroke-dasharray: 2 3; opacity: .7; }
  .label-ornament { fill: var(--accent); opacity: .28; }
  .brewery-arc { font-family: 'Noto Serif', serif; font-size: 9px; letter-spacing: 1px; fill: var(--ink); }
  .brand-name { font-family: 'Oswald', sans-serif; font-weight: 700; font-size: 62px; fill: var(--ink); }
  .flavour-name { font-family: 'Noto Serif', serif; font-weight: 700; font-size: 20px; fill: var(--ink); }
  .flavour-rule { stroke: var(--ink); stroke-width: 1.2; }
  .origin-ribbon { fill: var(--accent); }
  .origin-text { font-family: 'Roboto Condensed', sans-serif; font-weight: 700; font-size: 10px; letter-spacing: 3px; fill: var(--ribbon-text); }
  .spec-small { font-family: 'Roboto Condensed', sans-serif; font-weight: 700; font-size: 10px; fill: var(--ink); }
  .spec-volume { font-family: 'Roboto Condensed', sans-serif; font-weight: 700; font-size: 24px; fill: var(--ink); }
  .spec-abv { font-family: 'Roboto Condensed', sans-serif; font-weight: 700; font-size: 17px; fill: var(--ink); }
  .spec-unit { font-family: 'Roboto Condensed', sans-serif; font-weight: 700; font-size: 7px; fill: var(--ink); }
</style>
</head>
<body>
<main class="label-range">

  <svg class="label label--grapefruit" viewBox="0 0 290 470" aria-label="Mireille Grapefruit label">
    <defs><path id="arc-grapefruit" d="M78 177 Q145 140 212 177"/></defs>
    <path class="label-edge" d="M10 90 H28 Q30 70 45 60 Q145 -5 245 60 Q260 70 262 90 H280 Q290 90 290 100 V370 Q290 380 280 380 H262 Q260 400 245 410 Q145 470 45 410 Q30 400 28 380 H10 Q0 380 0 370 V100 Q0 90 10 90Z"/>
    <path class="label-stitch" transform="translate(14.5 23.5) scale(0.9)" d="M10 90 H28 Q30 70 45 60 Q145 -5 245 60 Q260 70 262 90 H280 Q290 90 290 100 V370 Q290 380 280 380 H262 Q260 400 245 410 Q145 470 45 410 Q30 400 28 380 H10 Q0 380 0 370 V100 Q0 90 10 90Z"/>
    <rect class="label-ornament" x="62" y="42" width="166" height="98" rx="14" role="img" aria-label="Ornamental filigree crest with arch"/>
    <text class="brewery-arc"><textPath href="#arc-grapefruit" startOffset="50%" text-anchor="middle">BRASSERIE CAP-AUBRY</textPath></text>
    <text class="brand-name" x="145" y="234" text-anchor="middle" textLength="232" lengthAdjust="spacingAndGlyphs">MIREILLE</text>
    <line class="flavour-rule" x1="30" y1="260" x2="58" y2="260"/><line class="flavour-rule" x1="232" y1="260" x2="260" y2="260"/>
    <text class="flavour-name" x="145" y="267" text-anchor="middle">GRAPEFRUIT</text>
    <rect class="label-ornament" x="120" y="281" width="50" height="24" rx="6" role="img" aria-label="Small ornamental flourish"/>
    <rect class="origin-ribbon" x="36" y="318" width="218" height="19"/>
    <text class="origin-text" x="145" y="331" text-anchor="middle">BRASSÉE AU QUÉBEC</text>
    <text class="spec-small" x="38" y="356">BIÈRE</text><text class="spec-small" x="38" y="367">BEER</text>
    <text class="spec-volume" x="145" y="367" text-anchor="middle">500 mL</text>
    <text class="spec-abv" x="236" y="358" text-anchor="middle">5%</text>
    <text class="spec-unit" x="236" y="367" text-anchor="middle">Alc./vol.</text>
  </svg>

  <svg class="label label--blueberry" viewBox="0 0 290 470" aria-label="Mireille Blueberry label">
    <defs><path id="arc-blueberry" d="M78 177 Q145 140 212 177"/></defs>
    <path class="label-edge" d="M10 90 H28 Q30 70 45 60 Q145 -5 245 60 Q260 70 262 90 H280 Q290 90 290 100 V370 Q290 380 280 380 H262 Q260 400 245 410 Q145 470 45 410 Q30 400 28 380 H10 Q0 380 0 370 V100 Q0 90 10 90Z"/>
    <path class="label-stitch" transform="translate(14.5 23.5) scale(0.9)" d="M10 90 H28 Q30 70 45 60 Q145 -5 245 60 Q260 70 262 90 H280 Q290 90 290 100 V370 Q290 380 280 380 H262 Q260 400 245 410 Q145 470 45 410 Q30 400 28 380 H10 Q0 380 0 370 V100 Q0 90 10 90Z"/>
    <rect class="label-ornament" x="62" y="42" width="166" height="98" rx="14" role="img" aria-label="Ornamental filigree crest with arch"/>
    <text class="brewery-arc"><textPath href="#arc-blueberry" startOffset="50%" text-anchor="middle">BRASSERIE CAP-AUBRY</textPath></text>
    <text class="brand-name" x="145" y="234" text-anchor="middle" textLength="232" lengthAdjust="spacingAndGlyphs">MIREILLE</text>
    <line class="flavour-rule" x1="34" y1="260" x2="62" y2="260"/><line class="flavour-rule" x1="228" y1="260" x2="256" y2="260"/>
    <text class="flavour-name" x="145" y="267" text-anchor="middle">BLUEBERRY</text>
    <rect class="label-ornament" x="120" y="281" width="50" height="24" rx="6" role="img" aria-label="Small ornamental flourish"/>
    <rect class="origin-ribbon" x="36" y="318" width="218" height="19"/>
    <text class="origin-text" x="145" y="331" text-anchor="middle">BRASSÉE AU QUÉBEC</text>
    <text class="spec-small" x="38" y="356">BIÈRE</text><text class="spec-small" x="38" y="367">BEER</text>
    <text class="spec-volume" x="145" y="367" text-anchor="middle">500 mL</text>
    <text class="spec-abv" x="236" y="358" text-anchor="middle">5%</text>
    <text class="spec-unit" x="236" y="367" text-anchor="middle">Alc./vol.</text>
  </svg>

  <svg class="label label--raspberry" viewBox="0 0 290 470" aria-label="Mireille Raspberry label">
    <defs><path id="arc-raspberry" d="M78 177 Q145 140 212 177"/></defs>
    <path class="label-edge" d="M10 90 H28 Q30 70 45 60 Q145 -5 245 60 Q260 70 262 90 H280 Q290 90 290 100 V370 Q290 380 280 380 H262 Q260 400 245 410 Q145 470 45 410 Q30 400 28 380 H10 Q0 380 0 370 V100 Q0 90 10 90Z"/>
    <path class="label-stitch" transform="translate(14.5 23.5) scale(0.9)" d="M10 90 H28 Q30 70 45 60 Q145 -5 245 60 Q260 70 262 90 H280 Q290 90 290 100 V370 Q290 380 280 380 H262 Q260 400 245 410 Q145 470 45 410 Q30 400 28 380 H10 Q0 380 0 370 V100 Q0 90 10 90Z"/>
    <rect class="label-ornament" x="62" y="42" width="166" height="98" rx="14" role="img" aria-label="Ornamental filigree crest with arch"/>
    <text class="brewery-arc"><textPath href="#arc-raspberry" startOffset="50%" text-anchor="middle">BRASSERIE CAP-AUBRY</textPath></text>
    <text class="brand-name" x="145" y="234" text-anchor="middle" textLength="232" lengthAdjust="spacingAndGlyphs">MIREILLE</text>
    <line class="flavour-rule" x1="30" y1="260" x2="58" y2="260"/><line class="flavour-rule" x1="232" y1="260" x2="260" y2="260"/>
    <text class="flavour-name" x="145" y="267" text-anchor="middle">RASPBERRY</text>
    <rect class="label-ornament" x="120" y="281" width="50" height="24" rx="6" role="img" aria-label="Small ornamental flourish"/>
    <rect class="origin-ribbon" x="36" y="318" width="218" height="19"/>
    <text class="origin-text" x="145" y="331" text-anchor="middle">BRASSÉE AU QUÉBEC</text>
    <text class="spec-small" x="38" y="356">BIÈRE</text><text class="spec-small" x="38" y="367">BEER</text>
    <text class="spec-volume" x="145" y="367" text-anchor="middle">500 mL</text>
    <text class="spec-abv" x="236" y="358" text-anchor="middle">5%</text>
    <text class="spec-unit" x="236" y="367" text-anchor="middle">Alc./vol.</text>
  </svg>

</main>
</body>
</html>
```